Product Label for Health Supplement

Design a product label to go on the jar. The product is a health supplement super-food called Moringa oleifera (Moringa leaf).

This product will be sold online at velarosa.com.au and in health-food stores. For inspiration, you can see Velarosa's 2 products on velarosa.com.au which are in a jar size similar to this new product.

The label needs to be attractive and feels natural and healthy.

A content template has been prepared for you. Please use all the content from the template in your design concept. There is no need to add new text. Please keep the text provided in the template.

The label has been setout in left, front, and right sides.
Here is the link to the template (also attached to the design brief) https://www.draftboardly.example/file/52TRgnXpq8LmZwYc3HbK4s/Untitled?type=design&node-id=0%3A1&t=QJ4rtLmNBwEpzYx7-1

Required Label Design Specifications:
Max Length: 275mm
Max Height: 70mm
DPI: 300 (at least)
Colour: CMYK
Minimum font: 5pt
Bleed: 1.5mm
Safe zone: 3mm from edge all around.

Once approved, the design will need to be delivered in CMYK color and in PDF format.

The Art Guidelines have been attached.

```html
<!DOCTYPE html>
<html lang="en">
<head>
<meta charset="utf-8">
<title>Velarosa Moringa Leaf Powder – Back Label</title>
<link rel="stylesheet" href="https://fonts.googleapis.com/css2?family=PT+Sans+Narrow:wght@400;700&family=Source+Sans+3:wght@400;600;700&display=swap">
<style>
  :root {
    --ink: #1f1f1f;
    --leaf-dark: #346b3c;
    --leaf-light: #8fc43f;
    --badge-green: #2ea84a;
    --paper: #ffffff;
    --rule: #2a2a2a;
  }
  * { box-sizing: border-box; margin: 0; padding: 0; }
  html, body { width: 1000px; height: 1200px; overflow: hidden; background: var(--paper); }
  body { position: relative; color: var(--ink); font-family: "Source Sans 3", sans-serif; }

  .label { position: absolute; left: 70px; top: 320px; width: 860px; height: 700px; }

  .usage-title { position: absolute; left: 0; top: 0; font-family: "PT Sans Narrow", sans-serif; font-weight: 700; font-size: 30px; letter-spacing: .3px; }
  .usage-text { position: absolute; left: 0; top: 42px; width: 840px; font-size: 23px; line-height: 1.38; }
  .ingredient { position: absolute; left: 0; top: 150px; font-size: 23px; }
  .ingredient strong { font-family: "PT Sans Narrow", sans-serif; font-weight: 700; }

  .nutrition { position: absolute; left: 0; top: 200px; width: 500px; height: 440px; border: 1.5px solid var(--rule); border-top: none; display: flex; flex-direction: column; }
  .nutrition-head { background: var(--leaf-dark); color: var(--paper); font-family: "PT Sans Narrow", sans-serif; padding: 8px 10px 10px; height: 104px; }
  .nutrition-head .title { font-weight: 700; font-size: 27px; line-height: 1.1; }
  .nutrition-head .meta { font-size: 20px; line-height: 1.2; }
  .nutrition-head .meta b { font-weight: 700; }
  .col-heads { display: grid; grid-template-columns: 120px 190px 190px; background: var(--leaf-light); color: var(--paper); font-size: 18px; text-align: center; line-height: 1.15; padding: 4px 0; }
  .rows { display: grid; grid-template-columns: 112px 190px 190px; padding: 12px 0 0 8px; font-size: 18px; row-gap: 7px; }
  .rows .name { font-family: "PT Sans Narrow", sans-serif; font-size: 17px; }
  .rows .val { text-align: center; }
  .footnote { margin-top: auto; padding: 0 0 10px 8px; font-family: "PT Sans Narrow", sans-serif; font-style: italic; font-size: 14px; }

  .side { position: absolute; left: 540px; top: 200px; width: 320px; }
  .storage { font-size: 19px; line-height: 1.3; }
  .company { margin-top: 34px; font-size: 24px; line-height: 1.3; font-style: normal; }
  .company .name { font-weight: 700; }
  .owned { margin-top: 16px; font-weight: 700; font-size: 24px; }
  .origin-badge { margin-top: 18px; display: flex; align-items: center; gap: 14px; width: 300px; height: 84px; border: 4px solid var(--badge-green); border-radius: 8px; padding: 0 14px; }
  .origin-badge p { font-weight: 700; font-size: 19px; line-height: 1.2; white-space: nowrap; }
</style>
</head>
<body>
<main class="label">
  <h2 class="usage-title">SUGGESTED USE :</h2>
  <p class="usage-text">Daily add 5g (1 teaspoon) to a glass of water and take it any time of day that’s convenient for you. You can also mix it with juice, coconut water, a smoothie, or your favourite protein shake!</p>
  <p class="ingredient"><strong>Ingredient:</strong> 100% NPOP Certified Organic Moringa oleifera leaf powder.</p>

  <section class="nutrition">
    <div class="nutrition-head">
      <p class="title">NUTRITION INFORMATION*</p>
      <p class="meta">SERVINGS PER PACKAGE: <b>30</b></p>
      <p class="meta">SERVING SIZE: <b>5g</b></p>
    </div>
    <div class="col-heads">
      <span></span><span>Average Quantity<br>per Serving</span><span>Average Quantity<br>per 100 g</span>
    </div>
    <div class="rows">
      <span class="name">Energy</span><span class="val">13 kJ (3 Cal)</span><span class="val">262 kJ (63 Cal)</span>
      <span class="name">Protein</span><span class="val">1.4 g</span><span class="val">28.8 g</span>
      <span class="name">Fat,Total</span><span class="val">0.3 g</span><span class="val">6.3 g</span>
      <span class="name">-Saturated</span><span class="val">0.0 g</span><span class="val">0.0 g</span>
      <span class="name">Carbohydrate</span><span class="val">1.0 g</span><span class="val">19.5 g</span>
      <span class="name">-Sugars</span><span class="val">less than 0.1 g</span><span class="val">0.8 g</span>
      <span class="name">Dietary Fibre</span><span class="val">2.5 g</span><span class="val">50.0 g</span>
      <span class="name">Sodium</span><span class="val">8 mg</span><span class="val">162 mg</span>
    </div>
    <p class="footnote">*Typical analysis</p>
  </section>

  <aside class="side">
    <p class="storage">Store below 25ºC in a cool dry place.<br>Ensure lid is tightly closed after use.</p>
    <address class="company">
      <span class="name">Velarosa</span><br>
      12 Wattlebird Ln<br>
      Sunnybank QLD 4109<br>
      AUSTRALIA<br>
      TEL: 1800 555 019<br>
      www.velarosa.com.au
    </address>
    <p class="owned">100% AUSTRALIAN OWNED</p>
    <div class="origin-badge">
      <svg width="72" height="30" viewBox="0 0 72 30" aria-hidden="true">
        <rect x="1" y="1" width="70" height="28" fill="none" stroke="var(--badge-green)" stroke-width="2"/>
        <path d="M22 29v-9M34 29v-9M46 29v-9M58 29v-9" stroke="var(--badge-green)" stroke-width="2"/>
      </svg>
      <p>Product of India<br>Packed in Australia</p>
    </div>
  </aside>
</main>
</body>
</html>
```